Property Management business needs Business cards designed

We provide a premium property management service based in Sydney's Norther Beaches. We want people to feel confident in choosing us to manage their investment properties. We offer a much more personalized service than other estate agents.
We want a modern clean design. Something that shows confidence without being complicated.
Logo attached.

Target Market(s)

35-70yo Male and Female with strong property portfolios within Sydney's Norther Beaches

Industry/Entity Type

Property Management

Contact Information for Business Card

Address: Suite 7, 18-19 Harlow Parade, Harlow Point NSW 2108
Two separate named cards.
Tom Carver - 0413 572 961 tom@harlowlettings.com.au
Marisol Ketter - 0408 167 543 marisol@harlowlettings.com.au

Requirements
Must have
• Business logo, name, number, address, email.

```html
<!DOCTYPE html>
<html lang="en">
<head>
<meta charset="utf-8">
<title>Harlow Lettings – Business Cards</title>
<link rel="stylesheet" href="https://fonts.googleapis.com/css2?family=PT+Sans:wght@400;700&display=swap">
<style>
  :root {
    --backdrop-top: #2b2b2b;
    --backdrop-bottom: #030303;
    --card-white: #ffffff;
    --brand-teal: #1a7a8c;
    --name-teal: #1d6b80;
    --ink: #111111;
    --on-teal: #ffffff;
  }
  * { margin: 0; padding: 0; box-sizing: border-box; }
  html, body { width: 1200px; height: 900px; overflow: hidden; }
  body {
    position: relative;
    background: linear-gradient(180deg, var(--backdrop-top) 0%, #1a1a1a 45%, var(--backdrop-bottom) 100%);
    font-family: "PT Sans", sans-serif;
  }
  .card {
    position: absolute;
    top: 306px;
    width: 440px;
    height: 271px;
    border-radius: 12px;
  }
  .card-front { left: 149px; background: var(--card-white); }
  .card-back { left: 608px; width: 441px; background: var(--brand-teal); }

  .front-wordmark {
    position: absolute;
    left: 27px;
    top: 55px;
    font-size: 31px;
    font-weight: 700;
    letter-spacing: -0.3px;
    color: var(--ink);
    line-height: 1;
  }
  .contact-block {
    position: absolute;
    left: 188px;
    top: 143px;
    color: var(--ink);
  }
  .contact-name {
    font-size: 17px;
    font-weight: 700;
    color: var(--name-teal);
    margin-bottom: 9px;
  }
  .contact-address {
    font-size: 13px;
    line-height: 16px;
    margin-bottom: 13px;
  }
  .contact-line {
    display: flex;
    align-items: center;
    font-size: 13px;
    line-height: 16px;
  }
  .contact-line svg { width: 10px; height: 10px; margin-right: 7px; flex: none; }
  .icon-phone { fill: var(--name-teal); }

  .back-wordmark {
    position: absolute;
    left: 0;
    right: 0;
    top: 104px;
    text-align: center;
    font-size: 46px;
    font-weight: 700;
    color: var(--on-teal);
    line-height: 1;
    letter-spacing: -0.3px;
  }
</style>
</head>
<body>
  <section class="card card-front" aria-label="Business card front">
    <div class="front-wordmark">HARLOW LETTINGS</div>
    <div class="contact-block">
      <p class="contact-name">Tom Carver</p>
      <p class="contact-address">Suite 7, 18-19 Harlow Parade<br>Harlow Point NSW 2108</p>
      <p class="contact-line">
        <svg class="icon-phone" viewBox="0 0 10 10" aria-hidden="true"><path d="M2 0.5 L3.6 2.6 L2.7 3.6 Q3.8 5.9 6.3 7.3 L7.3 6.3 L9.5 7.9 L8.3 9.5 Q4.5 9.4 1.8 6.5 Q0.3 4.4 0.5 1.6 Z"/></svg>
        0413 572 961
      </p>
      <p class="contact-line">
        <svg viewBox="0 0 10 10" aria-hidden="true"><rect x="0.5" y="2.2" width="9" height="5.8" fill="#1d6b80"/><path d="M1 2.7 L5 5.4 L9 2.7" fill="none" stroke="#ffffff" stroke-width="0.8"/></svg>
        tom@harlowlettings.com.au
      </p>
    </div>
  </section>

  <section class="card card-back" aria-label="Business card back">
    <div class="back-wordmark">HARLOW LETTINGS</div>
  </section>
</body>
</html>
```